We are looking for a HTML 5 Responsive Email design for our upcoming concierge services at Prestige Valmorena. We would like this page to be very visual and scream exclusivity and luxury.

We would like the title of the page to say “Take Advantage of Our Concierge Services”
Followed by an image of each of our services:

Luxury Car Hire
Yacht Rental
Private Chef
Dinner on a Yacht Experience
Private Wine Cellar
Airport Transfers
Baby-Sitting Services

Please add at the bottom of the page –
Please get in contact with us at concierge@prestigevalmorena-example.com

I have provided various images of each of some of the services, please choose which you believe are the best fit. (car services is hirequill) On the photo we would like a [Book Now] button.

Overall we would like this to be very visual but still user friendly.

I have attached our logo which should appear on the top left corner, please look at our website for inspiration – www.prestigevalmorena-example.com

Industry/Entity Type

Real Estate

Number of Pages Required

1 page

Font styles to use
Serif

Colors
85acd3
0355a3
ffffff
85cae6
3377b5

Requirements
Must have
• Very visual and eye pleasing. MUST BE A HTML EMAIL.

```html
<!DOCTYPE html>
<html lang="en">
<head>
<meta charset="utf-8">
<title>Prestige Valmorena – Concierge Services</title>
<link href="https://fonts.googleapis.com/css2?family=Montserrat:wght@600;700&family=Varela+Round&display=swap" rel="stylesheet">
<style>
:root{
  --brand-deep:#0355a3;
  --brand-mid:#3377b5;
  --brand-light:#85acd3;
  --sky:#85cae6;
  --white:#ffffff;
  --ink:#333a44;
  --muted:#666c75;
  --rule:#e6e8eb;
}
*{box-sizing:border-box;margin:0;padding:0}
html,body{width:737px;height:1200px;overflow:hidden;background:var(--white)}
body{position:relative;font-family:'Varela Round',Arial,sans-serif;color:var(--ink)}

/* header */
.site-header{position:absolute;left:0;top:0;width:737px;height:82px;border-bottom:1px solid var(--rule);background:var(--white)}
.brand{position:absolute;left:64px;top:22px;display:flex;align-items:center;gap:6px}
.brand-square{width:26px;height:26px;background:var(--brand-mid)}
.brand-name{font-size:10.5px;color:var(--brand-mid);letter-spacing:.5px;line-height:1.2;width:72px}
.top-bar{position:absolute;top:10px;right:72px;display:flex;align-items:center;gap:16px;white-space:nowrap}
.contact-line{font-size:8.3px;color:#555;display:flex;align-items:center;gap:5px}
.contact-line svg{width:9px;height:9px;flex:none}
.lang{font-size:7.5px;color:#333;display:flex;align-items:center;gap:5px;margin-left:4px}
.lang .flag{width:9px;height:6px;background:var(--brand-deep)}
.lang .caret{margin-left:18px;font-size:8px}
.main-nav{position:absolute;top:55px;left:413px;font-size:8.8px}
.main-nav a{color:#333;text-decoration:none;position:absolute;white-space:nowrap}
.main-nav a.active{color:var(--brand-deep)}

/* hero */
.hero{position:absolute;left:0;top:82px;width:737px;height:357px;background:linear-gradient(180deg,#c9cfd6 0%,#b7bcc0 30%,#d8cfc2 52%,#8a7a64 72%,#4f7b86 86%,#6a6c64 100%)}
.hero-title{position:absolute;left:116px;top:174px;width:506px;height:35px;background:rgba(3,85,163,.82);color:var(--white);font-size:21.5px;letter-spacing:1px;display:flex;align-items:center;justify-content:center;white-space:nowrap}
.hero-dots{position:absolute;left:328px;top:330px;width:81px;height:21px;background:rgba(0,0,0,.35);display:flex;align-items:center;justify-content:center;gap:10px}
.hero-dots span{width:7px;height:7px;border-radius:50%;background:rgba(255,255,255,.55)}
.hero-dots span.on{background:var(--white)}

.social-rail{position:absolute;left:0;top:116px;width:36px}
.social-rail span{display:block;width:36px;height:37.6px}

/* services */
.section-title{position:absolute;left:0;top:454px;width:737px;text-align:center;font-family:'Montserrat',Arial,sans-serif;font-weight:700;font-size:18px;letter-spacing:1px;color:var(--brand-deep)}
.tile{position:absolute;overflow:hidden}
.tile-photo{position:absolute;inset:0}
.tile-shade{position:absolute;inset:0;background:rgba(30,35,40,.35)}
.tile-label{position:absolute;left:0;right:0;top:50%;transform:translateY(-50%);display:flex;flex-direction:column;align-items:center}
.tile-label h3{font-weight:400;font-size:15.5px;color:var(--white);padding:4px 10px;border-top:1px solid rgba(255,255,255,.6);border-bottom:1px solid rgba(255,255,255,.6);white-space:nowrap;letter-spacing:.3px}
.book-now{position:absolute;left:91px;top:117px;width:81px;height:26px;background:var(--brand-deep);color:var(--white);font-family:'Montserrat',Arial,sans-serif;font-weight:700;font-size:10px;display:flex;align-items:center;justify-content:center;letter-spacing:.3px}

/* contact band */
.contact-band{position:absolute;left:61px;top:1074px;width:615px;height:78px;background:linear-gradient(180deg,var(--brand-mid),var(--brand-deep));color:var(--white);text-align:center}
.contact-band h2{margin-top:22px;font-family:'Montserrat',Arial,sans-serif;font-weight:700;font-size:14.5px;letter-spacing:.2px}
.contact-band p{margin-top:6px;font-size:10px;display:flex;align-items:center;justify-content:center;gap:8px}
.contact-band svg{width:10px;height:10px}

/* footer */
.footer-nav a{position:absolute;top:1171px;font-size:8.5px;color:#333;text-decoration:none}
.footer-nav a.active{color:var(--brand-deep)}
.copyright{position:absolute;right:65px;top:1172px;font-size:8.8px;color:#555}
</style>
</head>
<body>

<header class="site-header">
  <div class="brand">
    <span class="brand-square"></span>
    <span class="brand-name">Prestige Valmorena</span>
  </div>
  <div class="top-bar">
    <div class="contact-line">
      <svg viewBox="0 0 10 10"><path d="M2 1l2 2-1 1.2c.6 1.2 1.5 2.1 2.8 2.8L7 6l2 2-1.3 1.3C4.5 9 1 5.5.7 2.3z" fill="#666"/></svg>
      +34 900 123 456
    </div>
    <div class="contact-line">
      <svg viewBox="0 0 10 10"><rect x=".5" y="2" width="9" height="6.5" fill="none" stroke="#666"/><path d="M.5 2l4.5 3.5L9.5 2" fill="none" stroke="#666"/></svg>
      info@prestigevalmorena-example.com
    </div>
    <div class="lang"><span class="flag"></span>English<span class="caret">&#8964;</span></div>
  </div>
  <nav class="main-nav">
    <a class="active" style="left:0">Home</a>
    <a style="left:45px">About Us</a>
    <a style="left:104px">Services</a>
    <a style="left:157px">Blog</a>
    <a style="left:196px">Contact Us</a>
  </nav>
</header>

<section class="hero" role="img" aria-label="White Spanish-style villa with terracotta roof, lounge terrace and pool at dusk">
  <div class="hero-title">Take Advantage of Our Concierge Services</div>
  <div class="hero-dots"><span></span><span></span><span class="on"></span><span></span></div>
</section>

<div class="social-rail" aria-label="Social links">
  <span style="background:#1d5aa8"></span>
  <span style="background:#1da1e0"></span>
  <span style="background:#e0352b"></span>
  <span style="background:#b5770f"></span>
  <span style="background:#e32b2b"></span>
</div>

<h1 class="section-title">OUR SERVICES</h1>

<div class="tile" style="left:61px;top:495px;width:268px;height:184px">
  <div class="tile-photo" role="img" aria-label="Yellow sports car driving on a desert road" style="background:linear-gradient(160deg,#6b4a2a 0%,#a8763e 35%,#8a8a2a 60%,#2a2a22 100%)"></div>
  <div class="tile-shade" style="background:rgba(20,20,20,.25)"></div>
  <div class="tile-label" style="top:75px;transform:none"><h3>Luxury Car Hire</h3></div>
  <div class="book-now">BOOK NOW</div>
</div>

<div class="tile" style="left:339px;top:495px;width:163px;height:184px">
  <div class="tile-photo" role="img" aria-label="White motor yacht cruising on the sea" style="background:linear-gradient(180deg,#5b6168 0%,#7c8791 45%,#a9b0b6 70%,#6c757c 100%)"></div>
  <div class="tile-shade"></div>
  <div class="tile-label"><h3>Yacht Rental</h3></div>
</div>

<div class="tile" style="left:512px;top:495px;width:164px;height:184px">
  <div class="tile-photo" role="img" aria-label="Chef plating a dessert" style="background:linear-gradient(180deg,#1d1d1d 0%,#2f2b28 55%,#8a7a6a 85%,#c9c2b8 100%)"></div>
  <div class="tile-shade"></div>
  <div class="tile-label"><h3>Private Chef</h3></div>
</div>

<div class="tile" style="left:61px;top:687px;width:193px;height:184px">
  <div class="tile-photo" role="img" aria-label="Wine bottles racked in a wooden cellar" style="background:linear-gradient(90deg,#2a140c 0%,#5a2e18 40%,#8a5a30 75%,#3a2010 100%)"></div>
  <div class="tile-shade"></div>
  <div class="tile-label"><h3>Private Wine Cellar</h3></div>
</div>

<div class="tile" style="left:263px;top:687px;width:413px;height:184px">
  <div class="tile-photo" role="img" aria-label="Superyacht speeding past a wooded coastline" style="background:linear-gradient(180deg,#7c8a8e 0%,#5a6a55 35%,#b9bec2 55%,#2f4a62 80%,#1e3550 100%)"></div>
  <div class="tile-shade"></div>
  <div class="tile-label"><h3>Dinner on a Yacht Experience</h3></div>
</div>

<div class="tile" style="left:61px;top:880px;width:302px;height:184px">
  <div class="tile-photo" role="img" aria-label="Travellers with luggage beside a limousine and private jet" style="background:linear-gradient(180deg,#cfd3d6 0%,#a7adb2 45%,#6c6e70 75%,#4a4a4a 100%)"></div>
  <div class="tile-shade"></div>
  <div class="tile-label"><h3>Airport Transfers</h3></div>
</div>

<div class="tile" style="left:373px;top:880px;width:303px;height:184px">
  <div class="tile-photo" role="img" aria-label="Colourful wooden letter blocks spelling baby sitter" style="background:linear-gradient(180deg,#8a8a8a 0%,#a68a4a 35%,#8a4a3a 55%,#5a6a8a 75%,#8a8a8a 100%)"></div>
  <div class="tile-shade"></div>
  <div class="tile-label"><h3>Baby-Sitting Services</h3></div>
</div>

<section class="contact-band">
  <h2>PLEASE GET IN CONTACT WITH US AT</h2>
  <p>
    <svg viewBox="0 0 10 10"><rect x=".5" y="2" width="9" height="6.5" fill="none" stroke="#fff"/><path d="M.5 2l4.5 3.5L9.5 2" fill="none" stroke="#fff"/></svg>
    concierge@prestigevalmorena-example.com
  </p>
</section>

<nav class="footer-nav">
  <a class="active" style="left:69px">Home</a>
  <a style="left:114px">About Us</a>
  <a style="left:172px">Services</a>
  <a style="left:226px">Blog</a>
  <a style="left:264px">Contact Us</a>
</nav>
<div class="copyright">Copyright &copy; Prestige Valmorena 2017</div>

</body>
</html>
```